Pet Dryer Package Box Design

The original design which is from our team member and failed is attached below. Also, the package size is attached in the files.
We need to design the package of the pet dryer for an innovative pet product company called "MORVEX". We developed innovative pet products for pet owners. We want to see designs that send signals of innovation and superiority to customers to increase the price premium. The original package design is attached below. The original version is denied by Halbrook because they don't think our package shows the product worth $300. We want designs that local Americans think are worth the premium.

Target Market(s)

Pet Market

Requirements
Must have
• Our product picture and logo

```html
<!DOCTYPE html>
<html lang="en">
<head>
<meta charset="utf-8">
<title>MORVEX Pet Hair Dryer – Box Dieline</title>
<link href="https://fonts.googleapis.com/css2?family=Montserrat:wght@800&family=Barlow+Condensed:wght@400;500;600;700&display=swap" rel="stylesheet">
<style>
  :root{
    --blue:#2a7ba0;
    --blue-deep:#1d6688;
    --blue-light:#3e93b8;
    --gold:#d9b57c;
    --kraft:#dfc293;
    --white:#ffffff;
    --ink:#1d3c4f;
    --grey:#e9edf0;
    --page:#ffffff;
  }
  html,body{margin:0;padding:0;width:1200px;height:1200px;overflow:hidden;background:var(--page);}
  .dieline{display:block;width:1200px;height:1200px;}
  .brand{font-family:"Montserrat",sans-serif;font-weight:800;}
  .cond{font-family:"Barlow Condensed",sans-serif;}
  .tagline{font-family:"Barlow Condensed",sans-serif;font-weight:500;fill:var(--gold);letter-spacing:.3px;}
  .headline{font-family:"Barlow Condensed",sans-serif;font-weight:700;fill:var(--white);}
  .label{font-family:"Barlow Condensed",sans-serif;font-weight:600;fill:var(--ink);}
  .fold{stroke:#ffffff;stroke-width:1.4;stroke-dasharray:6 4;fill:none;opacity:.85;}
  .fold-dark{stroke:#b9c4cc;stroke-width:1.2;stroke-dasharray:6 4;fill:none;}
  .icon-ring{fill:var(--blue);stroke:var(--gold);stroke-width:2.5;}
  .icon-glyph{fill:none;stroke:#fff;stroke-width:2;stroke-linecap:round;}
  .leader{stroke:#2b2b2b;stroke-width:1.2;fill:none;}
</style>
</head>
<body>
<svg class="dieline" viewBox="190 525 1560 1560" xmlns="http://www.w3.org/2000/svg">
  <defs>
    <linearGradient id="photo-tone" x1="0" y1="0" x2="1" y2="1">
      <stop offset="0" stop-color="#f7f8f9"/>
      <stop offset=".6" stop-color="#dfe4e8"/>
      <stop offset="1" stop-color="#b9c2c9"/>
    </linearGradient>
    <radialGradient id="blow-glow" cx=".5" cy=".45" r=".6">
      <stop offset="0" stop-color="#8fd2ef"/>
      <stop offset=".55" stop-color="#3e93b8"/>
      <stop offset="1" stop-color="#2a7ba0"/>
    </radialGradient>

    <g id="front-face">
      <rect x="593" y="1225" width="392" height="337" fill="var(--white)"/>
      <rect x="593" y="1477" width="392" height="85" fill="var(--blue)"/>
      <path d="M605 1225 H742 V1437 a10 10 0 0 1 -10 10 H615 a10 10 0 0 1 -10 -10 Z" fill="var(--blue)" stroke="var(--gold)" stroke-width="2.5"/>
      <text class="brand" x="616" y="1268" font-size="24" fill="var(--white)" textLength="116" lengthAdjust="spacingAndGlyphs">MORVEX</text>
      <text class="tagline" x="617" y="1283" font-size="11" textLength="115" lengthAdjust="spacingAndGlyphs">CARE THAT KEEPS MOVING</text>
      <rect x="617" y="1360" width="58" height="15" fill="var(--gold)"/>
      <text class="cond" x="619" y="1373" font-size="15" font-weight="600" fill="var(--ink)">AIR PRO</text>
      <text class="headline" x="616" y="1402" font-size="31">PET HAIR</text>
      <text class="headline" x="615" y="1438" font-size="42">DRYER</text>

      <g>
        <circle class="icon-ring" cx="811" cy="1268" r="17"/>
        <circle class="icon-glyph" cx="811" cy="1270" r="8"/>
        <path class="icon-glyph" d="M811 1270 l4 -4 M808 1259 h6"/>
        <text class="label" x="811" y="1300" font-size="9.5" text-anchor="middle">Faster</text>
        <text class="label" x="811" y="1310" font-size="9.5" text-anchor="middle">Drying</text>
      </g>
      <g>
        <circle class="icon-ring" cx="863" cy="1268" r="17"/>
        <path class="icon-glyph" d="M863 1258 v13"/>
        <circle cx="863" cy="1275" r="4" fill="#fff"/>
        <path class="icon-glyph" d="M868 1260 h3 M868 1264 h3 M868 1268 h3"/>
        <text class="label" x="863" y="1300" font-size="9.5" text-anchor="middle">Temperature</text>
        <text class="label" x="863" y="1310" font-size="9.5" text-anchor="middle">Control</text>
      </g>
      <g>
        <circle class="icon-ring" cx="914" cy="1268" r="17"/>
        <path class="icon-glyph" d="M905 1264 h4 l6 -5 v18 l-6 -5 h-4 Z"/>
        <path class="icon-glyph" d="M919 1262 l4 4 M923 1262 l-4 4"/>
        <text class="label" x="914" y="1300" font-size="9.5" text-anchor="middle">Noise</text>
        <text class="label" x="914" y="1310" font-size="9.5" text-anchor="middle">Reduction</text>
      </g>

      <rect x="757" y="1335" width="213" height="200" rx="22" fill="url(#photo-tone)" role="img" aria-label="Product photo: white pet drying box with a cat sitting behind the glass window"/>

      <rect x="607" y="1494" width="38" height="33" rx="3" fill="var(--gold)"/>
      <text class="cond" x="626" y="1521" font-size="24" font-weight="700" fill="var(--ink)" text-anchor="middle">60L</text>
      <text class="cond" x="607" y="1541" font-size="9.5" fill="var(--white)">Can hold max 2 little</text>
      <text class="cond" x="607" y="1551" font-size="9.5" fill="var(--white)">kittens at the same time</text>
    </g>
  </defs>

  <g class="top-lid">
    <path d="M593 1225 V845 a15 15 0 0 1 15 -15 H970 a15 15 0 0 1 15 15 V1225 Z" fill="var(--blue)"/>
    <path class="fold" d="M597 880 H981"/>
    <rect x="617" y="898" width="343" height="305" rx="14" fill="var(--white)"/>
    <text class="brand" x="788" y="1055" font-size="46" fill="var(--blue)" text-anchor="middle" textLength="236" lengthAdjust="spacingAndGlyphs">MORVEX</text>
    <text class="tagline" x="788" y="1083" font-size="21" text-anchor="middle" textLength="236" lengthAdjust="spacingAndGlyphs">CARE THAT KEEPS MOVING</text>
  </g>

  <path class="dust-flap" d="M245 1225 L282 1072 Q290 1048 315 1048 H520 Q545 1048 553 1072 L593 1225 Z" fill="var(--blue)"/>
  <path class="dust-flap" d="M985 1225 L1025 1072 Q1033 1048 1058 1048 H1262 Q1287 1048 1295 1072 L1333 1225 Z" fill="var(--blue)"/>

  <path class="glue-tab" d="M245 1232 L215 1245 Q208 1248 208 1256 V1560 Q208 1568 215 1570 L245 1580 Z" fill="var(--blue)"/>

  <g class="side-left">
    <rect x="245" y="1225" width="348" height="337" fill="var(--blue)"/>
    <text class="brand" x="268" y="1268" font-size="24" fill="var(--white)" textLength="116" lengthAdjust="spacingAndGlyphs">MORVEX</text>
    <text class="tagline" x="268" y="1283" font-size="11" textLength="115" lengthAdjust="spacingAndGlyphs">CARE THAT KEEPS MOVING</text>
    <rect x="262" y="1292" width="314" height="223" rx="10" fill="var(--white)"/>
    <rect x="275" y="1318" width="165" height="170" rx="20" fill="url(#photo-tone)" role="img" aria-label="Product drawing: pet drying box with labelled parts"/>

    <g class="features">
      <path class="leader" d="M372 1320 H464"/>
      <path class="leader" d="M357 1347 L374 1362 H470"/>
      <path class="leader" d="M418 1420 L432 1404 H448"/>
      <path class="leader" d="M368 1432 L380 1445 H476"/>
      <path class="leader" d="M335 1455 L365 1487 H449"/>
      <text class="label" x="531" y="1322" font-size="9.5" fill="var(--blue)" text-anchor="end">Intelligent Control</text>
      <text class="label" x="531" y="1364" font-size="9.5" fill="var(--blue)" text-anchor="end">Noise Reduction</text>
      <text class="label" x="531" y="1406" font-size="9.5" fill="var(--blue)" text-anchor="end">Windows of Petting Pet</text>
      <text class="label" x="531" y="1447" font-size="9.5" fill="var(--blue)" text-anchor="end">Glass Visibility</text>
      <text class="label" x="531" y="1489" font-size="9.5" fill="var(--blue)" text-anchor="end">Fresh Wind Circulation</text>
      <circle class="icon-ring" cx="548" cy="1319" r="11"/>
      <path class="icon-glyph" d="M546 1324 v-9 M546 1319 h5 v5"/>
      <circle class="icon-ring" cx="548" cy="1361" r="11"/>
      <path class="icon-glyph" d="M543 1359 h3 l4 -4 v12 l-4 -4 h-3 Z"/>
      <circle class="icon-ring" cx="548" cy="1403" r="11"/>
      <circle class="icon-glyph" cx="548" cy="1403" r="5"/>
      <circle class="icon-ring" cx="548" cy="1444" r="11"/>
      <rect class="icon-glyph" x="543" y="1439" width="10" height="10"/>
      <path class="icon-glyph" d="M543 1446 l7 -7 M546 1449 l7 -7"/>
      <circle class="icon-ring" cx="548" cy="1486" r="11"/>
      <path class="icon-glyph" d="M541 1483 h10 a2.5 2.5 0 1 0 -2.5 -2.5 M541 1488 h12 a2.5 2.5 0 1 1 -2.5 2.5"/>
    </g>

    <text class="cond" x="268" y="1538" font-size="17" font-weight="500" fill="var(--white)">morvex USA LCC</text>
    <text class="cond" x="268" y="1549" font-size="8" fill="var(--white)">MADE IN CHINA</text>
    <rect x="465" y="1532" width="104" height="17" rx="2" fill="var(--gold)"/>
    <text class="cond" x="517" y="1545" font-size="11.5" font-weight="600" fill="var(--ink)" text-anchor="middle">www.morvexusa.com</text>
  </g>

  <use href="#front-face"/>
  <use href="#front-face" x="740"/>

  <g class="side-right">
    <rect x="985" y="1225" width="348" height="337" fill="var(--blue)"/>
    <rect x="1010" y="1290" width="300" height="230" fill="url(#blow-glow)" opacity=".75"/>
    <text class="cond" x="1006" y="1268" font-size="29" font-weight="600" fill="var(--gold)" letter-spacing=".5">UNIQUE BLOWING</text>
    <text class="cond" x="1006" y="1296" font-size="29" font-weight="600" fill="var(--white)" letter-spacing=".5">DESIGN</text>
    <rect x="1072" y="1315" width="176" height="178" rx="22" fill="url(#photo-tone)" role="img" aria-label="Product render: pet drying box with blue airflow arrows inside"/>
    <text class="cond" x="1006" y="1550" font-size="29" font-weight="600" fill="var(--white)" letter-spacing=".5">CERTIFICATIONS</text>
    <path d="M1211 1522 V1556" stroke="var(--gold)" stroke-width="2"/>
    <circle cx="1229" cy="1538" r="9" fill="var(--white)"/>
    <rect x="1245" y="1528" width="24" height="20" rx="3" fill="var(--white)"/>
    <rect x="1276" y="1528" width="30" height="20" rx="3" fill="var(--white)"/>
  </g>

  <g class="bottom">
    <rect x="245" y="1562" width="1480" height="22" fill="var(--kraft)"/>
    <path d="M245 1584 H593 L420 1690 L445 1778 H245 Z" fill="var(--kraft)"/>
    <path d="M593 1584 H985 V1800 H870 V1757 H705 V1800 H593 Z" fill="var(--kraft)"/>
    <path d="M985 1584 H1333 V1778 H1135 L1160 1690 Z" fill="var(--kraft)"/>
    <path d="M1333 1584 H1725 L1615 1740 L1620 1800 H1430 L1435 1745 Z" fill="var(--kraft)"/>
  </g>

  <g>
    <path class="fold" d="M245 1225 H1725"/>
    <path class="fold" d="M245 1225 V1580 M593 1225 V1580 M985 1225 V1580 M1333 1225 V1580"/>
    <path class="fold-dark" d="M245 1581 H1725"/>
    <path class="fold-dark" d="M593 1584 V1795 M985 1584 V1795 M1333 1584 V1780"/>
  </g>
</svg>
</body>
</html>
```